Bright Fern Custom Homes business card. Double sided. Modern. professional

Bright Fern Custom Homes
contemporary modern design with our logo /
Double sided with all our contact information
Use same Green colors as in our Logo. Contemporary logo that grabs your attention. Visually pleasing and balanced. Easy to read, and Vibrant. Would love an option for rounded edges. Embossed logo would be amazing.
Contact Information for Business Card
Dana Welk Owner / General Contractor Bright Fern Custom Homes p: 704.552.1830 m: 912.648.2071 e: brightferncustomhomes@mailbox.example w: www.brightferncustomhomes.example 218 Pryor Meadow Lane Batesburg, SC 29041

```html
<!DOCTYPE html>
<html lang="en">
<head>
<meta charset="utf-8">
<title>Bright Fern Custom Homes — Business Card</title>
<link rel="stylesheet" href="https://fonts.googleapis.com/css2?family=Cinzel:wght@400;600&family=Roboto+Condensed:wght@400&family=Arimo:wght@400&display=swap">
<style>
  :root {
    --backdrop: #7b7b7b;
    --fern: #728e38;
    --fern-deep: #5f7a2c;
    --fern-logo: #6b8a31;
    --charcoal: #222222;
    --white: #ffffff;
  }
  * { margin: 0; padding: 0; box-sizing: border-box; }
  html, body {
    width: 1133px;
    height: 1200px;
    overflow: hidden;
    background: var(--backdrop);
  }
  .card {
    position: absolute;
    left: 197px;
    width: 728px;
    height: 416px;
    border-radius: 26px;
    overflow: hidden;
  }
  .card--front { top: 140px; background: var(--fern); color: var(--white); }
  .card--back { top: 642px; background: var(--charcoal); }

  .front-emblem {
    position: absolute;
    left: 330px;
    top: 40px;
    width: 340px;
    height: 340px;
    border-radius: 50%;
    background: var(--fern-deep);
    opacity: 0.55;
  }
  .identity {
    position: absolute;
    left: 43px;
    top: 142px;
  }
  .identity__name {
    font-family: "Cinzel", serif;
    font-weight: 600;
    font-size: 25px;
    line-height: 28px;
    letter-spacing: 0.5px;
  }
  .identity__role {
    font-family: "Roboto Condensed", sans-serif;
    font-size: 16px;
    line-height: 18px;
    letter-spacing: 0.6px;
  }
  .address {
    position: absolute;
    left: 43px;
    top: 222px;
    font-family: "Arimo", sans-serif;
    font-size: 16px;
    line-height: 21px;
    font-style: normal;
  }
  .contact-list {
    position: absolute;
    left: 43px;
    top: 292px;
    list-style: none;
    font-family: "Arimo", sans-serif;
    font-size: 16px;
    line-height: 21px;
  }
  .contact-list li { display: flex; align-items: center; }
  .contact-list svg { width: 14px; height: 14px; margin-right: 8px; fill: var(--white); flex: none; }

  .brand {
    position: absolute;
    left: 0;
    right: 0;
    top: 118px;
    text-align: center;
    color: var(--fern-logo);
    font-family: "Cinzel", serif;
    font-weight: 400;
  }
  .brand__mark {
    width: 96px;
    height: 96px;
    margin: 0 auto 52px;
    border-radius: 50%;
    background: var(--fern-logo);
  }
  .brand__name {
    font-size: 38px;
    line-height: 40px;
    letter-spacing: 1px;
  }
  .brand__tagline {
    font-size: 11px;
    line-height: 12px;
    letter-spacing: 9px;
    margin-top: 0;
    padding-left: 9px;
  }
</style>
</head>
<body>
  <section class="card card--front" aria-label="Card front">
    <div class="front-emblem" aria-hidden="true"></div>

    <div class="identity">
      <h1 class="identity__name">DANA WELK</h1>
      <p class="identity__role">Owner/General Contractor</p>
    </div>

    <address class="address">
      218 Pryor<br>
      Meadow Lane<br>
      Batesburg, SC 29041
    </address>

    <ul class="contact-list">
      <li>
        <svg viewBox="0 0 24 24" aria-hidden="true"><path d="M6.6 10.8a15.1 15.1 0 0 0 6.6 6.6l2.2-2.2a1 1 0 0 1 1-.25 11.4 11.4 0 0 0 3.6.57 1 1 0 0 1 1 1V20a1 1 0 0 1-1 1A17 17 0 0 1 3 4a1 1 0 0 1 1-1h3.5a1 1 0 0 1 1 1c0 1.25.2 2.45.57 3.6a1 1 0 0 1-.25 1z"/></svg>
        704.552.1830
      </li>
      <li>
        <svg viewBox="0 0 24 24" aria-hidden="true"><path d="M7 1h10a2 2 0 0 1 2 2v18a2 2 0 0 1-2 2H7a2 2 0 0 1-2-2V3a2 2 0 0 1 2-2zm0 3v15h10V4z"/></svg>
        912.648.2071
      </li>
      <li>
        <svg viewBox="0 0 24 24" aria-hidden="true"><path d="M2 5h20v14H2zm2 2v.5l8 5 8-5V7l-8 5z"/></svg>
        brightferncustomhomes@mailbox.example
      </li>
      <li>
        <svg viewBox="0 0 24 24" aria-hidden="true"><path d="M12 2a10 10 0 1 0 0 20 10 10 0 0 0 0-20zm-1 17.9A8 8 0 0 1 4.1 9.8L9 14.7v1a2 2 0 0 0 2 2zm6.9-2.5A2 2 0 0 0 16 16h-1v-3a1 1 0 0 0-1-1H8v-2h2a1 1 0 0 0 1-1V7h2a2 2 0 0 0 2-2v-.4a8 8 0 0 1 2.9 12.8z"/></svg>
        brightferncustomhomes.example
      </li>
    </ul>
  </section>

  <section class="card card--back" aria-label="Card back">
    <div class="brand">
      <div class="brand__mark" aria-hidden="true"></div>
      <p class="brand__name">BRIGHT FERN</p>
      <p class="brand__tagline">CUSTOM HOMES</p>
    </div>
  </section>
</body>
</html>
```